WanderKinMates Website (Travel VLog/BLOG)

Need to finish the development of our wordpress website. Template is a child template on top of its parent framework named "Pebble Scaffold". Knowledge of pebble scaffold and use with word press is not needed. BUt a plus for the design effort. The majority of the design changes done using custom CSS and the base child sheets.

Information:
Website modifications have started:
What is needed:
1. www.wanderkinmates.example is currently using a CMS engine the idea is to migrate the main page (www.wanderkinmates.example) as well as the picture gallery for http://www.wanderkinmates.example/gallery all over to wordpress.

2. Design/finish home page of www.wanderkinmates.example/blog to have all the functionality as stated in images 1 and 2 of attached document/screenshots
3. Continue using current theme and logos as similar on the site
4. Front page should have NEWLETTER/SUBSCRIBER FORM
5. Front page should have SOCIAL MEDIA FEED option as it is currently on (www.wanderkinmates.example)
6. Provide multiple WKM themed template pages to be used for secondary and tertiary supporting pages.
7. Secondary pages should be in 2 and three column configurations with menu bar header/footer palcement

Alternate designs are welcomed we will decided accordingly. Please remember this is strictly a TRAVEL VLOG/BLOG site. SO that theme is key.

Also the idea is to use the least amount of plugins to get this site up and running properly.

Target Market(s)

Travel/Tourism Blogging

Industry/Entity Type

Travel

Coding

Coded - Design and coding required

Number of Pages Required

5+ page

Font styles to use
Sans Serif

Colors
f37122
ffffff
faa54b
85cae6
d0dfed
919191
d3d3d3

Requirements
Must have
• 1.Subscriber form/newsletter popup
• 2.Social Media feeds on front page: (Instagram, twitter, Facebook)
• 3.Most recent video
• 4. Photo Gallery preview
• 5. format that somewhat relates to our images, but not too cartoon like. Just professional and theme based
• 6. Less dark colors (ways to remove as many greys and blacks from the website)
• 7. 1/2/3 column formatted wordpress template pages that can be used for site content.
• 8. FULLY RESPONSIZE and compatible with all browsers.
Nice to have
• This is not a nice to have, I am just using this box to reach out to you:
• Your the experts. We are suggesting colors to you below, and we've also added information on what was adapted to the current website. We are looking for your guidance,creativity, and suggestions on how this site should come to life. And though we have not committed to paying we have full intent of picking a designer. This website is new to us, and to commit to something that we have never used or heard about before is somewhat concerning. Please also understand the member will be a part of our team meaning they will get credit for their work and they can use it as a reference for future work they may be introduced to.
Should not have
• Should not rely on too many external addon/plugins. We would prefer this site to stay code based and not turn into a gui WYSIWYG site which needs plugins to stay online and purchased

```html
<!DOCTYPE html>
<html lang="en">
<head>
<meta charset="utf-8">
<title>Roamwell Travel Guide</title>
<link rel="stylesheet" href="https://fonts.googleapis.com/css2?family=Lato:wght@400;700;900&family=Montserrat:wght@600;700&display=swap">
<style>
:root{
  --orange:#f37122;
  --orange-light:#faa54b;
  --sky:#85cae6;
  --sky-deep:#4fb0de;
  --mist:#d0dfed;
  --card:#e9f0f7;
  --grey:#919191;
  --grey-light:#d3d3d3;
  --text:#333b44;
  --body:#7a7f86;
  --white:#ffffff;
  --page:#f3f6f9;
}
*{box-sizing:border-box;margin:0;padding:0}
html,body{width:1200px;height:2528px;overflow:hidden}
body{font-family:"Lato",Arial,sans-serif;color:var(--text);background:var(--page)}
.canvas{position:relative;width:1200px;height:2528px;overflow:hidden;background:var(--page)}
.abs{position:absolute}

/* header */
.site-header{position:absolute;left:0;top:0;width:1200px;height:88px;background:var(--white)}
.brand{position:absolute;left:155px;top:28px;display:flex;align-items:center;gap:10px}
.brand-dot{width:30px;height:30px;border-radius:50%;background:var(--orange)}
.brand-name{font-weight:700;font-size:22px;color:var(--orange)}
.main-nav{position:absolute;left:0;top:38px;font-size:15px;color:var(--orange)}
.main-nav span{position:absolute;white-space:nowrap}
.search-icon{position:absolute;left:1014px;top:37px}

/* hero */
.hero{position:absolute;left:0;top:92px;width:1200px;height:500px;
  background:linear-gradient(180deg,#9fd0ee 0%,#cfe8f5 22%,#6e9a52 45%,#4e8a48 55%,#58c3c9 72%,#9fe0dc 88%,var(--page) 100%)}
.hero-title{position:absolute;left:152px;top:255px;font-family:"Montserrat",Arial,sans-serif;font-weight:700;font-size:40px;line-height:42px;color:var(--white);letter-spacing:.5px}
.btn-more{position:absolute;left:153px;top:357px;width:130px;height:36px;background:var(--sky);color:var(--white);font-size:14px;line-height:36px;text-align:center}
.hero-dots{position:absolute;left:162px;top:417px;display:flex;gap:8px}
.hero-dots i{width:12px;height:12px;border-radius:50%;background:var(--white);display:block}
.hero-dots i:first-child{background:transparent;border:2px solid var(--white)}

/* content panel */
.content-panel{position:absolute;left:145px;top:581px;width:913px;height:1576px;background:var(--white)}

.tab{position:absolute;top:600px;height:42px;color:var(--white);font-size:15px;font-weight:700;display:flex;align-items:center;justify-content:center;gap:10px}
.tab svg{flex:none}
.tab-news{left:174px;width:200px;background:var(--sky)}
.tab-offer{left:381px;width:202px;background:var(--orange)}
.tab-hot{left:586px;width:203px;background:var(--orange-light)}

.section-title{position:absolute;font-size:20px;font-weight:700;color:var(--orange);letter-spacing:.3px}
.section-title.blue{color:var(--sky)}

.photo{position:absolute}
.play{position:absolute;left:50%;top:50%;width:38px;height:38px;margin:-19px 0 0 -19px;border-radius:50%;background:var(--white);display:flex;align-items:center;justify-content:center}
.play::after{content:"";border-left:11px solid #222;border-top:7px solid transparent;border-bottom:7px solid transparent;margin-left:3px}

.video-meta{position:absolute;width:202px}
.video-title{font-size:15px;color:var(--sky)}
.video-text{font-size:11px;color:var(--body);margin-top:6px;white-space:nowrap;overflow:hidden}
.video-date{font-size:11px;color:var(--orange);margin-top:9px}

.teaser-card{position:absolute;top:972px;height:197px;background:var(--card);padding:32px 30px 0 30px}
.teaser-card h4{font-size:14px;line-height:19px;color:#4a86b6;font-weight:700}
.teaser-card p{font-size:11px;line-height:17px;color:var(--body);margin-top:10px}
.teaser-card small{display:block;font-size:10px;color:#5d7fa1;margin-top:10px}

/* sidebar */
.newsletter{position:absolute;left:812px;top:607px;width:221px;height:177px;background:var(--sky);padding:18px 20px}
.newsletter h3{font-size:19px;font-weight:400;color:var(--white)}
.newsletter p{font-size:9px;line-height:13px;color:#eaf6fb;margin-top:4px}
.newsletter .field{margin-top:10px;height:28px;background:var(--white);font-size:10px;color:var(--grey);padding:0 10px;line-height:28px}
.newsletter .subscribe{margin-top:8px;width:93px;height:28px;background:var(--orange);color:var(--white);font-size:12px;line-height:28px;text-align:center}
.ad{position:absolute;left:812px;width:221px}

/* popular */
.arrow-btn{position:absolute;top:1207px;width:24px;height:24px;border-radius:50%;background:#e6e8eb;display:flex;align-items:center;justify-content:center}
.article-item{position:absolute;left:753px;width:250px}
.article-item h5{font-size:14px;font-weight:400;color:var(--text)}
.article-item p{font-size:11px;line-height:17px;color:var(--body);margin-top:5px}

/* lower block */
.lower-block{position:absolute;left:177px;top:1527px;width:848px;height:604px;border:1px solid var(--grey-light)}
.col-head{position:absolute;height:41px;font-size:14px;line-height:41px;padding-left:18px}
.head-blogs{left:177px;top:1527px;width:404px;background:linear-gradient(180deg,var(--orange-light),var(--orange));color:var(--white)}
.head-cooking{left:581px;top:1527px;width:222px;background:var(--sky);color:var(--white)}
.head-friends{left:803px;top:1527px;width:222px;background:#f1f3f5;color:var(--text);font-size:16px;border-bottom:1px solid var(--grey-light)}
.col-rule{position:absolute;top:1527px;width:1px;height:604px;background:var(--grey-light)}

.blog-item{position:absolute;left:352px;width:215px}
.blog-item h5{font-size:15px;line-height:20px;font-weight:400;color:var(--text)}
.blog-item p{font-size:11px;line-height:17px;color:var(--body);margin-top:6px}
.blog-item small{display:block;font-size:11px;color:var(--orange);margin-top:6px}

.cook-text{position:absolute;left:581px;top:1703px;width:222px;text-align:center}
.cook-text h5{font-size:15px;font-weight:400}
.cook-text p{font-size:11px;line-height:17px;color:var(--body);margin-top:6px;padding:0 14px}
.cook-text a{display:block;font-size:12px;color:var(--sky);margin-top:8px;text-decoration:none}
.head-gallery{left:581px;top:1828px;width:222px;background:#eef0f2;color:var(--text);font-size:15px;height:38px;line-height:38px}
.slider-arrow{position:absolute;top:1615px;width:22px;height:34px;background:rgba(40,40,40,.75);display:flex;align-items:center;justify-content:center}

.feed-item{position:absolute;left:822px;width:195px;display:flex;gap:10px}
.avatar{flex:none;width:30px;height:30px;background:#b7a08a}
.feed-item .txt{font-size:11px;line-height:15px;color:var(--text)}
.feed-item .txt span{color:var(--body);font-size:10px}
.feed-item .txt em{display:block;font-style:normal;color:#3b6fb6;font-size:10px;margin-top:4px}
.head-chirp{left:803px;top:1764px;width:222px;height:40px;line-height:40px;background:var(--sky-deep);color:var(--white);font-size:16px}
.follow-btn{position:absolute;left:968px;top:1775px;width:50px;height:18px;border-radius:3px;background:var(--white);color:var(--sky-deep);font-size:10px;line-height:18px;text-align:center;font-weight:700}
.chirp-item{position:absolute;left:822px;width:180px}
.chirp-item .who{display:flex;gap:8px;font-size:12px;color:var(--text)}
.chirp-item .who span{display:block;font-size:10px;color:var(--body)}
.chirp-item p{font-size:10px;line-height:15px;color:var(--body);margin-top:8px}
.chirp-item em{display:block;font-style:normal;font-size:10px;color:var(--sky-deep);margin-top:6px}
.scroll-track{position:absolute;left:1013px;top:1806px;width:7px;height:270px;background:#eceff2}
.scroll-thumb{position:absolute;left:1013px;top:1848px;width:7px;height:40px;background:#c4c9ce}

/* footer */
.footer-wave{position:absolute;left:0;top:2130px}
.site-footer{position:absolute;left:0;top:2200px;width:1200px;height:328px;background:linear-gradient(180deg,#9ed3ec,#72bde3)}
.foot-col{position:absolute;top:2248px}
.foot-col h6{font-size:17px;font-weight:400;color:var(--white);letter-spacing:.5px}
.foot-col ul{list-style:none;margin-top:14px}
.foot-col li{font-size:12px;color:#eef8fd;line-height:26.5px}
.contact-line{position:absolute;display:flex;align-items:center;gap:8px;color:var(--white)}
.social-row{position:absolute;left:765px;top:2389px;display:flex;gap:6px}
.social-row i{display:block;width:26px;height:26px;border-radius:50%;border:1.5px solid var(--white)}
.foot-rule{position:absolute;left:160px;top:2474px;width:900px;height:1px;background:rgba(255,255,255,.6)}
.copyright{position:absolute;left:0;top:2492px;width:1200px;text-align:center;font-size:11px;color:var(--white)}
</style>
</head>
<body>
<div class="canvas">

  <header class="site-header">
    <div class="brand"><span class="brand-dot"></span><span class="brand-name">Roamwell Travel Guide</span></div>
    <nav class="main-nav">
      <span style="left:408px">ABOUT</span>
      <span style="left:483px">NEW SERVICES</span>
      <span style="left:611px">DESTINATIONS</span>
      <span style="left:741px">GALLERY</span>
      <span style="left:828px">CONTACTS</span>
      <span style="left:936px">BLOG</span>
    </nav>
    <svg class="search-icon" width="16" height="16" viewBox="0 0 16 16"><circle cx="6.5" cy="6.5" r="5" fill="none" stroke="#919191" stroke-width="2"/><line x1="10.2" y1="10.2" x2="15" y2="15" stroke="#919191" stroke-width="2"/></svg>
  </header>

  <section class="hero" role="img" aria-label="Tropical bay with limestone cliffs, turquoise water and long-tail boats on the beach"></section>
  <h1 class="hero-title">WELCOME TO ROAMWELL<br>TRAVEL GUIDE</h1>
  <div class="btn-more">MORE INFO</div>
  <div class="hero-dots"><i></i><i></i><i></i><i></i></div>

  <div class="content-panel"></div>

  <div class="tab tab-news">
    <svg width="24" height="18" viewBox="0 0 24 18"><rect x="1" y="1" width="22" height="16" fill="none" stroke="#fff" stroke-width="1.6"/><rect x="4" y="4" width="7" height="6" fill="#fff"/><line x1="13" y1="5" x2="20" y2="5" stroke="#fff" stroke-width="1.4"/><line x1="13" y1="9" x2="20" y2="9" stroke="#fff" stroke-width="1.4"/><line x1="4" y1="13" x2="20" y2="13" stroke="#fff" stroke-width="1.4"/></svg>
    News &amp; Events</div>
  <div class="tab tab-offer">
    <svg width="20" height="20" viewBox="0 0 20 20"><path d="M2 2h8l8 8-8 8-8-8z" fill="none" stroke="#fff" stroke-width="1.8"/><circle cx="6" cy="6" r="1.6" fill="#fff"/></svg>
    What We Offer</div>
  <div class="tab tab-hot">
    <svg width="22" height="22" viewBox="0 0 22 22"><rect x="3" y="9" width="12" height="10" fill="none" stroke="#fff" stroke-width="1.8"/><line x1="9" y1="9" x2="9" y2="19" stroke="#fff" stroke-width="1.6"/><circle cx="17" cy="5" r="3" fill="none" stroke="#fff" stroke-width="1.6"/></svg>
    Hot Tours</div>

  <h2 class="section-title" style="left:177px;top:674px">MOST RECENT VIDEOS</h2>

  <div class="photo" style="left:174px;top:716px;width:202px;height:164px;background:linear-gradient(180deg,#5aa6dd,#c9b490 60%,#e7d7b7)" role="img" aria-label="Thatched beach umbrella and loungers on white sand"><span class="play"></span></div>
  <div class="photo" style="left:382px;top:716px;width:203px;height:164px;background:linear-gradient(180deg,#2f8fd6,#8fc9e8 55%,#e9dcc2)" role="img" aria-label="Traveller relaxing under palm trees by the sea"><span class="play"></span></div>
  <div class="photo" style="left:590px;top:716px;width:204px;height:164px;background:linear-gradient(180deg,#8fa8a8,#4a7a6a 50%,#2d4a46)" role="img" aria-label="Couple in a boat among karst islands"><span class="play"></span></div>

  <div class="video-meta" style="left:174px;top:888px"><div class="video-title">Video Tittle here</div><div class="video-text">sociosqu ad litora torquent per con</div><div class="video-date">24, Nov 2016</div></div>
  <div class="video-meta" style="left:382px;top:888px"><div class="video-title">Video Tittle here</div><div class="video-text">sociosqu ad litora torquent per con</div><div class="video-date">24, Nov 2016</div></div>
  <div class="video-meta" style="left:590px;top:888px"><div class="video-title">Video Tittle here</div><div class="video-text">sociosqu ad litora torquent per con</div><div class="video-date">24, Nov 2016</div></div>

  <article class="teaser-card" style="left:174px;width:202px"><h4>Curabitur metus ipsum luctus malesuada</h4><p>sociosqu ad litora torquent per conubia nostra per inceptos hymenaeos</p><small>Posted 02 Nov 2016</small></article>
  <article class="teaser-card" style="left:377px;width:210px;background:#edf3f9"><h4>Proin nulla arcu nonu mmy luctus dictu</h4><p>sociosqu ad litora torquent per conubia nostra per inceptos hymenaeos</p><small>Posted 02 Nov 2016</small></article>
  <article class="teaser-card" style="left:588px;width:206px"><h4>Maecenas aliquet velit vel turpis Mauri</h4><p>sociosqu ad litora torquent per conubia nostra per inceptos hymenaeos</p><small>Posted 02 Nov 2016</small></article>

  <aside class="newsletter">
    <h3>Newsletter Sign Up</h3>
    <p>sociosqu ad litora torquent per conubia nostra per inceptos hymen</p>
    <div class="field">Email address</div>
    <div class="subscribe">Subscribe</div>
  </aside>
  <div class="ad" style="top:794px;height:183px;background:linear-gradient(180deg,#f7d98a,#e7a94c 80%,#7a4a8a 88%,#5b3270)" role="img" aria-label="Sponsored banner for a pet adoption campaign"></div>
  <div class="ad" style="top:986px;height:183px;background:linear-gradient(180deg,#f58a2a,#e2631c 60%,#111 62%,#111 80%,#f3f3f3 82%)" role="img" aria-label="Sponsored banner for a college evening classes program"></div>

  <h2 class="section-title" style="left:179px;top:1205px">FEATURED VIDEO</h2>
  <div class="photo" style="left:177px;top:1249px;width:409px;height:232px;background:linear-gradient(160deg,#1c6fc8,#5bb4e8 45%,#2f8a68 70%,#d9d1b5)" role="img" aria-label="Palm tree leaning over a tropical beach with green islands"><span class="play"></span></div>

  <h2 class="section-title blue" style="left:617px;top:1205px">POPULAR ARTICLES</h2>
  <div class="arrow-btn" style="left:970px"><svg width="8" height="10" viewBox="0 0 8 10"><path d="M6 1L2 5l4 4" fill="none" stroke="#919191" stroke-width="1.6"/></svg></div>
  <div class="arrow-btn" style="left:1002px"><svg width="8" height="10" viewBox="0 0 8 10"><path d="M2 1l4 4-4 4" fill="none" stroke="#919191" stroke-width="1.6"/></svg></div>

  <div class="photo" style="left:620px;top:1249px;width:116px;height:67px;background:linear-gradient(180deg,#9fb8b8,#4f6f66)" role="img" aria-label="Traveller overlooking a bay"></div>
  <div class="photo" style="left:620px;top:1331px;width:116px;height:68px;background:linear-gradient(180deg,#f2b544,#9a5a1e)" role="img" aria-label="Sunset over a field"></div>
  <div class="photo" style="left:620px;top:1415px;width:116px;height:66px;background:linear-gradient(180deg,#8ccbe6,#3c94c8)" role="img" aria-label="Woman relaxing by the sea"></div>
  <div class="article-item" style="top:1247px"><h5>Olypian quarrels et gorilla</h5><p>sociosqu ad litora torquent per conubia nostra per inceptos hymenaeos Proin nulla arcu non</p></div>
  <div class="article-item" style="top:1334px"><h5>Maecenas aliquet velit vel</h5><p>sociosqu ad litora torquent per conubia nostra per inceptos hymenaeos Proin nulla arcu non</p></div>
  <div class="article-item" style="top:1418px"><h5>Donec quis mi sed magna hen</h5><p>sociosqu ad litora torquent per conubia nostra per inceptos hymenaeos Proin nulla arcu non</p></div>

  <div class="lower-block"></div>
  <div class="col-rule" style="left:581px"></div>
  <div class="col-rule" style="left:803px"></div>
  <div class="col-head head-blogs">LATEST FROM THE BLOGS</div>
  <div class="col-head head-cooking">COOKING ARTICLES</div>
  <div class="col-head head-friends">Friends Feed</div>

  <div class="photo" style="left:199px;top:1591px;width:140px;height:101px;background:linear-gradient(135deg,#d89a5a,#8a5a3a)" role="img" aria-label="Backpacker on a trail"></div>
  <div class="photo" style="left:199px;top:1722px;width:140px;height:101px;background:linear-gradient(180deg,#2c8ee0,#8fd3ea 55%,#e4d6b5)" role="img" aria-label="Beach loungers under palms"></div>
  <div class="photo" style="left:199px;top:1859px;width:140px;height:101px;background:linear-gradient(135deg,#3fa8c8,#1f6f8f)" role="img" aria-label="Swimmer in a turquoise pool"></div>
  <div class="photo" style="left:205px;top:1987px;width:140px;height:103px;background:linear-gradient(180deg,#7fc2ea,#4aa3c7 55%,#e8dcc0)" role="img" aria-label="Palm-lined city beach"></div>

  <div class="blog-item" style="top:1590px"><h5>Donec quis mi sed magna hen</h5><p>sociosqu ad litora torquent per conubia nostra per inceptos hymenaeos lorem Nunc porta convallis pede</p><small>NOVEMBER 25, 2016</small></div>
  <div class="blog-item" style="top:1718px"><h5>Proin dui lectus cursus eu mattis laoreet viverra sit</h5><p>sociosqu ad litora torquent per conubia nostra per inceptos hymenaeos</p><small>NOVEMBER 25, 2016</small></div>
  <div class="blog-item" style="top:1858px"><h5>Maecenas aliquet velit vel</h5><p>sociosqu ad litora torquent per conubia nostra per inceptos hymenaeos lorem Nunc porta convallis pede</p><small>NOVEMBER 25, 2016</small></div>
  <div class="blog-item" style="left:357px;top:1988px"><h5>Etiam eleifend metus vitae adi</h5><p>sociosqu ad litora torquent per conubia nostra per inceptos hymenaeos lorem Nunc porta convallis pede</p><small>NOVEMBER 25, 2016</small></div>

  <div class="photo" style="left:583px;top:1574px;width:218px;height:116px;background:linear-gradient(135deg,#e9e6e1,#b9c59a 50%,#d9784a)" role="img" aria-label="Bowls of fresh salads and vegetables on a table"></div>
  <div class="slider-arrow" style="left:581px"><svg width="7" height="12" viewBox="0 0 7 12"><path d="M6 1L1 6l5 5" fill="none" stroke="#fff" stroke-width="1.6"/></svg></div>
  <div class="slider-arrow" style="left:781px"><svg width="7" height="12" viewBox="0 0 7 12"><path d="M1 1l5 5-5 5" fill="none" stroke="#fff" stroke-width="1.6"/></svg></div>
  <div class="cook-text"><h5>Article Tittle here</h5><p>sociosqu ad litora torquent per conu bia nostra per inceptos hym</p><a>READ MORE</a></div>
  <div class="col-head head-gallery">OUR GALLERY</div>

  <div class="photo" style="left:600px;top:1879px;width:89px;height:67px;background:linear-gradient(180deg,#1b2a4a,#3a5a8a)" role="img" aria-label="Bridge lit at night"></div>
  <div class="photo" style="left:699px;top:1879px;width:90px;height:67px;background:linear-gradient(180deg,#8fc3e6,#c98a5a)" role="img" aria-label="Canal with boats"></div>
  <div class="photo" style="left:600px;top:1960px;width:89px;height:67px;background:linear-gradient(180deg,#9cc8ea,#8a8a5a)" role="img" aria-label="Ancient stepped pyramid"></div>
  <div class="photo" style="left:699px;top:1960px;width:90px;height:67px;background:linear-gradient(180deg,#2a3a6a,#c2703a)" role="img" aria-label="Harbour statue at dusk"></div>
  <div class="photo" style="left:600px;top:2040px;width:89px;height:70px;background:linear-gradient(180deg,#c04a2a,#3a6a3a)" role="img" aria-label="Colourful domed cathedral"></div>
  <div class="photo" style="left:699px;top:2040px;width:90px;height:70px;background:linear-gradient(180deg,#a9c9e0,#d6a862)" role="img" aria-label="Desert pyramids"></div>

  <div class="feed-item" style="top:1584px"><span class="avatar"></span><div class="txt">Lorem ipsum dolor sit amet consectetuer <span>@ inceptos hymenaeos Cum sociis natoque penatibus et magnis dis</span><em>2 days ago</em></div></div>
  <div class="feed-item" style="top:1678px"><span class="avatar" style="background:#8a7a6a"></span><div class="txt">Quisque dignissim congue <span>@ inceptos hymenaeos Cum sociis natoque penatibus et</span><em>2 days ago</em></div></div>

  <div class="col-head head-chirp">Chirp Feed</div>
  <div class="follow-btn">Follow</div>
  <div class="chirp-item" style="top:1820px"><div class="who"><span class="avatar" style="background:#6a5a5a"></span><div>Vestibulum ligula<span>@ inceptos hymenaeos</span></div></div><p>Curabitur metus ipsum luctus eu malesuada ut tincidunt sed diam Donec quis mi sed magna hen</p><em>2 days ago</em></div>
  <div class="chirp-item" style="top:1938px"><div class="who"><span class="avatar" style="background:#9a7a5a"></span><div>Maecenas aliquet<span>@ inceptos hymenaeos</span></div></div><p>Curabitur metus ipsum luctus eu malesuada ut tincidunt sed diam Donec quis mi sed magna</p><em>2 days ago</em></div>
  <div class="scroll-track"></div><div class="scroll-thumb"></div>

  <svg class="footer-wave" width="1200" height="80" viewBox="0 0 1200 80" preserveAspectRatio="none"><path d="M0 30 C300 90 600 75 860 50 C1000 36 1110 22 1200 10 L1200 80 L0 80 Z" fill="#cde9f6"/><path d="M0 45 C300 100 620 85 880 62 C1020 50 1120 38 1200 28 L1200 80 L0 80 Z" fill="#9ed3ec"/></svg>
  <footer class="site-footer"></footer>

  <div class="foot-col" style="left:180px"><h6>QUICK LINKS</h6><ul><li>About Us</li><li>My Story</li><li>How it Works</li><li>Menu</li></ul></div>
  <div class="foot-col" style="left:374px"><h6>RESOURCES</h6><ul><li>Recipes</li><li>Blogs &amp; Articles</li><li>Testimonials</li><li>Courses</li></ul></div>
  <div class="foot-col" style="left:568px"><h6>SUBLINKS</h6><ul><li>Lorem ipsum</li><li>Solor sit amet</li><li>consectetuer adipiscing</li><li>Elit Nam cursus</li></ul></div>
  <div class="foot-col" style="left:762px"><h6>CONTACT INFO</h6></div>

  <div class="contact-line" style="left:762px;top:2286px;align-items:flex-start">
    <svg width="16" height="24" viewBox="0 0 16 24"><path d="M8 1C4 1 1 4 1 8c0 5 7 14 7 14s7-9 7-14c0-4-3-7-7-7z" fill="#fff"/><circle cx="8" cy="8" r="2.6" fill="#85cae6"/></svg>
    <span style="font-size:13px;line-height:22px">410 Harbor Lantern Way Suite 12<br>Brookmere, OR 97000</span>
  </div>
  <div class="contact-line" style="left:762px;top:2344px;font-size:16px">
    <svg width="18" height="18" viewBox="0 0 18 18"><path d="M4 1l3 4-2 2c1 2 3 4 5 5l2-2 4 3-2 3C8 16 2 10 1 4z" fill="none" stroke="#fff" stroke-width="1.5"/></svg>
    555 014 2287
  </div>
  <div class="contact-line" style="left:912px;top:2344px;font-size:14px">
    <svg width="20" height="18" viewBox="0 0 20 18"><path d="M2 2h16v10H8l-4 4v-4H2z" fill="none" stroke="#fff" stroke-width="1.5"/></svg>
    Send a message
  </div>
  <div class="social-row"><i></i><i></i><i></i><i></i></div>

  <div class="foot-rule"></div>
  <div class="copyright">© 2016 Company Name &nbsp;All right reserved</div>
</div>
</body>
</html>
```